Bradwell Business Card

I have a logo that I would like to use to design the Business Card for Bradwell Construction LLC. We are a commercial general contractor in San Antonio Texas. Id like a simple and sleek design. Message me if you have any questions. Thanks

Industry/Entity Type

Contractor

```html
<!DOCTYPE html>
<html lang="en">
<head>
<meta charset="utf-8">
<title>Bradwell Construction LLC – Business Card</title>
<link href="https://fonts.googleapis.com/css2?family=Arimo:wght@400;700&display=swap" rel="stylesheet">
<style>
  :root {
    --stage: #58595b;
    --white: #ffffff;
    --footer-grey: #d1d2d4;
    --brand-blue: #3a6cb5;
    --navy: #06357a;
    --ink: #3c3c3e;
    --ink-soft: #58595b;
  }
  * { margin: 0; padding: 0; box-sizing: border-box; }
  html, body {
    width: 1200px; height: 383px; overflow: hidden;
    background: var(--stage);
    font-family: "Arimo", Arial, sans-serif;
  }
  .stage { position: relative; width: 1200px; height: 383px; }

  .card {
    position: absolute; top: 42px; width: 522px; height: 298px;
    border-radius: 8px; overflow: hidden;
  }
  .card--front { left: 43px; background: var(--white); }
  .card--back { left: 629px; background: var(--navy); }

  /* Front */
  .front__tab {
    position: absolute; left: 0; top: 40px; width: 12px; height: 64px;
    background: var(--brand-blue); border-radius: 0 3px 3px 0;
  }
  .wordmark {
    position: absolute; font-weight: 700; line-height: 1;
    letter-spacing: -0.2px; text-transform: uppercase;
  }
  .wordmark__line { display: block; }
  .front__wordmark { left: 26px; top: 84px; color: var(--ink); }
  .front__wordmark .wordmark__line--main { font-size: 17px; }
  .front__wordmark .wordmark__line--sub { font-size: 13.5px; margin-top: 1px; }

  .person {
    position: absolute; left: 402px; top: 53px;
    padding-left: 9px; border-left: 2px solid var(--brand-blue);
    color: var(--ink);
  }
  .person__name { font-size: 12px; line-height: 14px; }
  .person__role { font-size: 8px; line-height: 10px; margin-top: 2px; }

  .front__footer {
    position: absolute; left: 0; top: 205px; width: 100%; height: 93px;
    background: var(--footer-grey);
  }
  .front__band {
    position: absolute; left: 25px; top: 205px; width: 472px; height: 8px;
    background: var(--brand-blue);
  }
  .contact {
    position: absolute; font-size: 8.5px; color: var(--ink);
    list-style: none;
  }
  .contact li { display: flex; align-items: center; height: 10px; margin-bottom: 8px; }
  .contact svg { width: 10px; height: 10px; margin-right: 10px; fill: var(--brand-blue); flex: none; }
  .contact--phones { left: 25px; top: 232px; }
  .contact--web { left: 178px; top: 232px; }
  .contact--address { left: 323px; top: 230px; line-height: 18px; }
  .contact--address li { align-items: flex-start; height: auto; }
  .contact--address svg { margin-top: 1px; width: 9px; height: 11px; margin-right: 10px; }

  /* Back */
  .back__rule {
    position: absolute; left: 49px; top: 53px; width: 2px; height: 102px;
    background: var(--white);
  }
  .back__wordmark { left: 78px; top: 121px; color: var(--white); }
  .back__wordmark .wordmark__line--main { font-size: 20px; }
  .back__wordmark .wordmark__line--sub { font-size: 15.5px; margin-top: 1px; }
</style>
</head>
<body>
<main class="stage">

  <section class="card card--front" aria-label="Business card front">
    <div class="front__tab"></div>
    <div class="wordmark front__wordmark">
      <span class="wordmark__line wordmark__line--main">Bradwell</span>
      <span class="wordmark__line wordmark__line--sub">Construction LLC</span>
    </div>

    <div class="person">
      <p class="person__name">Marcus Delane</p>
      <p class="person__role">CEO</p>
    </div>

    <div class="front__footer"></div>
    <div class="front__band"></div>

    <ul class="contact contact--phones">
      <li>
        <svg viewBox="0 0 10 10" aria-hidden="true"><path d="M2 0.5 L3.6 2.8 L2.8 3.8 C3.4 5.2 4.6 6.4 6 7 L7 6.2 L9.4 7.8 L8.6 9.4 C4.8 9.6 0.4 5.2 0.5 1.4 Z"/></svg>
        +0404318762
      </li>
      <li>
        <svg viewBox="0 0 10 10" aria-hidden="true"><path d="M2.5 0 H7.5 V10 H2.5 Z M3.4 1.2 V7.6 H6.6 V1.2 Z M4.4 8.3 H5.6 V9.2 H4.4 Z" fill-rule="evenodd"/></svg>
        +0404318762
      </li>
    </ul>

    <ul class="contact contact--web">
      <li>
        <svg viewBox="0 0 10 10" aria-hidden="true"><path d="M0 2 H10 V8.5 H0 Z M0.8 2.6 L5 5.6 L9.2 2.6 Z" fill-rule="evenodd"/></svg>
        info@bradwellbuild.com
      </li>
      <li>
        <svg viewBox="0 0 10 10" aria-hidden="true"><circle cx="5" cy="5" r="4.3" fill="none" stroke="#3a6cb5" stroke-width="1"/><ellipse cx="5" cy="5" rx="1.8" ry="4.3" fill="none" stroke="#3a6cb5" stroke-width="0.8"/><path d="M0.7 5 H9.3 M1.4 2.8 H8.6 M1.4 7.2 H8.6" stroke="#3a6cb5" stroke-width="0.7"/></svg>
        www.bradwellbuild.com
      </li>
    </ul>

    <ul class="contact contact--address">
      <li>
        <svg viewBox="0 0 9 11" aria-hidden="true"><path d="M4.5 0 C2 0 0 2 0 4.4 C0 7.4 4.5 11 4.5 11 C4.5 11 9 7.4 9 4.4 C9 2 7 0 4.5 0 Z M4.5 2.6 A1.8 1.8 0 1 1 4.49 2.6 Z" fill-rule="evenodd"/></svg>
        <span>Suite 12/ Level 6, 218 Harbour Row Drive,<br>Riverside, VIC 3010</span>
      </li>
    </ul>
  </section>

  <section class="card card--back" aria-label="Business card back">
    <div class="back__rule"></div>
    <div class="wordmark back__wordmark">
      <span class="wordmark__line wordmark__line--main">Bradwell</span>
      <span class="wordmark__line wordmark__line--sub">Construction LLC</span>
    </div>
  </section>

</main>
</body>
</html>
```